Very new and innovative Web design for Property managers of Vacation rentals

We are looking for a new website design for travel agencies and property managers specialised on vacation rentals business, holiday villas and apartments.

The end users of this website are travellers who are looking for a vacation home for their next holiday: this is the reason why the website must be easy to use, attractive, professional, possibly elegant and focused on get new reservations.

This is a draft of our current website: https://demo5.holdiquay.com/
Please consider that we would like to have proposals with a totally different and innovative layout, surprise us!

These are the pages of the website:
• Homepage: feel free to redesign all the homepage as you wish, surprise us with something very new! Please consider that Property manager/Travel agencies usually want to have the opportunity to put in evidence groups of houses with specific characteristics (eg. villas with private swimming pool, apartment in big/small towns, villas with air co, etc…), destinations and tourist areas, and sometimes experiences or activities (please consider that the website layout must be suitable even if some of the previous sections are not used).
• Search page: we’d like to organise the results of the search page in three different ways:
o Grid
o Map
o List
• Property page: to illustrate the characteristics, descriptions, images, …. of the property. It is very important to put in evidence images of the property and to maintain the booking form (and the other call to action bottom – eg. whatsapp) always visible
• Custom pages: static pages composed usually by text, images and call to actions
• Contact us (general form)
• Info request (specific of a property form)
• Booking process
• Blog, organised in four pages:
o Home Page – introduction to the blog
o List of articles
o Single article
o Site Map (presentation of categories and sub-categories)

If possible, we’d prefer to receive the material in Adobe XD or similar so that we can obtain the three versions:
- smartphone
- tablet
- desktop

The website will be then developed in Bootstrap: as a result we’ll need the icons in SVG format (or the library used)

In attachment you can find the map of the website pages

```html
<!DOCTYPE html>
<html lang="en">
<head>
<meta charset="utf-8">
<title>StayNest – Exclusive Villas in Italy</title>
<link href="https://fonts.googleapis.com/css2?family=Montserrat:wght@600;700&family=Roboto:wght@400;500;700&display=swap" rel="stylesheet">
<style>
:root{
  --green:#17b88a;
  --teal:#0d5f6b;
  --dark:#111;
  --text:#555;
  --grey-band:#e9ecee;
  --white:#fff;
}
*{box-sizing:border-box;margin:0;padding:0}
html,body{width:1200px;height:3005px;overflow:hidden}
body{position:relative;font-family:Roboto,Arial,sans-serif;color:var(--text);background:var(--white)}
.abs{position:absolute}
.hero{left:0;top:0;width:1200px;height:662px;background:linear-gradient(180deg,#8a8f93 0%,#a9b4ba 20%,#8fc0d8 34%,#5fa8cf 44%,#b9cdd6 56%,#d7dbdd 70%,#8d9093 100%)}
.logo{font-family:Roboto,sans-serif;font-weight:500;font-size:40px;color:var(--white);display:flex;align-items:center;gap:10px}
.logo .mark{width:34px;height:34px;border-radius:50%;background:var(--green)}
.nav{display:flex;gap:23px;font-weight:500;font-size:15px;color:var(--white)}
.nav .active{color:var(--green)}
.call{display:flex;align-items:center;gap:14px;color:var(--white)}
.call .ring{width:42px;height:42px;border:2px solid var(--white);border-radius:50%;display:flex;align-items:center;justify-content:center}
.call small{display:block;color:var(--green);font-size:13px}
.call b{font-size:16px;font-weight:500}
.hero-title{left:0;width:1200px;top:288px;text-align:center;font-family:Montserrat,sans-serif;font-weight:700;font-size:36px;color:var(--dark)}
.g{color:var(--green)}
.search{left:111px;top:595px;width:977px;height:135px;background:linear-gradient(90deg,var(--green) 0%,var(--teal) 60%,#0b4f63 100%);display:flex;align-items:center;gap:10px;padding:0 21px}
.field{height:50px;border-radius:25px;background:var(--white);display:flex;align-items:center;justify-content:space-between;padding:0 16px;font-size:16px;color:#555}
.btn{background:var(--green);color:var(--white);font-weight:700;font-size:16px;border-radius:26px;display:flex;align-items:center;justify-content:center;text-transform:uppercase}
h2{font-family:Montserrat,sans-serif;font-weight:700;color:var(--dark);text-transform:uppercase}
.about-text{left:111px;top:893px;width:474px;font-size:14.5px;line-height:24px;text-align:justify}
.about-text p+p{margin-top:13px}
.photo-frame{left:643px;top:822px;width:445px;height:373px;background:var(--white);box-shadow:0 2px 10px rgba(0,0,0,.2);padding:7px}
.ph{width:100%;height:100%}
.band{left:0;top:1294px;width:1200px;height:588px}
.card{top:1416px;width:311px;height:360px;background:var(--white);padding:5px;box-shadow:0 1px 4px rgba(0,0,0,.1)}
.card .ph{height:200px}
.card h3{font-size:18px;font-weight:500;color:var(--dark);margin:22px 8px 10px;text-transform:uppercase}
.card p{font-size:14.5px;line-height:22px;margin:0 8px;height:68px}
.card a{display:flex;align-items:center;gap:10px;margin:8px 8px 0;color:var(--green);font-weight:500;font-size:14.5px;text-decoration:none}
.dot{top:1813px;width:16px;height:16px;border-radius:50%}
.arrow{top:2283px;width:36px;height:36px;border-radius:50%;display:flex;align-items:center;justify-content:center}
.info{left:636px;top:2325px;width:358px;height:283px;background:var(--white);padding:26px 30px;box-shadow:0 1px 6px rgba(0,0,0,.1)}
.info small{color:var(--green);font-size:13px;font-weight:500}
.info h3{font-size:24px;font-weight:500;color:var(--dark);margin:12px 0 14px}
.info .meta{color:var(--green);font-size:14px;display:flex;gap:22px;margin-bottom:16px;align-items:center}
.info .meta span{display:flex;align-items:center;gap:10px}
.info p{font-size:14.5px;line-height:23px;text-align:justify}
.footer{left:0;top:2707px;width:1200px;height:298px;background:#000;color:var(--white)}
.fnav{left:0;width:1200px;top:30px;display:flex;justify-content:center;gap:26px;font-weight:500;font-size:17px}
.rule{left:111px;width:977px;height:1px;background:#444}
.fcol h4{font-weight:500;font-size:17px;margin-bottom:12px}
.fcol .row{font-size:15.5px;line-height:30px;display:flex;gap:18px}
.fcol .row svg{margin-top:9px;flex:none}
.social{top:2827px;width:42px;height:42px;border-radius:50%;background:var(--white)}
</style>
</head>
<body>

<div class="abs hero" role="img" aria-label="Photo of a bright villa lounge with grey sofas opening onto a sea view terrace"></div>

<div class="abs logo" style="left:111px;top:32px"><span class="mark"></span>StayNest</div>
<div class="abs call" style="left:892px;top:12px">
  <span class="ring"><svg width="16" height="16" viewBox="0 0 24 24" fill="#fff"><path d="M6.6 10.8a15 15 0 0 0 6.6 6.6l2.2-2.2a1 1 0 0 1 1-.25 11.4 11.4 0 0 0 3.6.57 1 1 0 0 1 1 1V20a1 1 0 0 1-1 1A17 17 0 0 1 3 4a1 1 0 0 1 1-1h3.5a1 1 0 0 1 1 1c0 1.25.2 2.45.57 3.57a1 1 0 0 1-.25 1z"/></svg></span>
  <span><small>Call Us</small><b>+39 055 0100200</b></span>
</div>
<nav class="abs nav" style="right:112px;top:64px">
  <span class="active">Home</span><span>Property/Unit</span><span>Booking Process</span><span>Blog StayNest</span><span>Contact Us</span>
</nav>

<h1 class="abs hero-title"><span class="g">EXCLUSIVE</span> VILLAS IN ITALY</h1>

<form class="abs search">
  <div class="field" style="width:188px">Destination<svg width="10" height="14" viewBox="0 0 10 14"><path d="M5 0a5 5 0 0 0-5 5c0 4 5 9 5 9s5-5 5-9a5 5 0 0 0-5-5zm0 7a2 2 0 1 1 0-4 2 2 0 0 1 0 4z" fill="#17b88a"/></svg></div>
  <div class="field" style="width:177px">Check In<svg width="14" height="14" viewBox="0 0 14 14"><rect x="1" y="2" width="12" height="11" fill="none" stroke="#17b88a" stroke-width="1.5"/><path d="M1 5h12M4 0v3M10 0v3" stroke="#17b88a" stroke-width="1.5"/></svg></div>
  <div class="field" style="width:177px">Check Out<svg width="14" height="14" viewBox="0 0 14 14"><rect x="1" y="2" width="12" height="11" fill="none" stroke="#17b88a" stroke-width="1.5"/><path d="M1 5h12M4 0v3M10 0v3" stroke="#17b88a" stroke-width="1.5"/></svg></div>
  <div class="field" style="width:177px">Travelers<svg width="12" height="14" viewBox="0 0 12 14"><circle cx="6" cy="4" r="3.5" fill="#17b88a"/><path d="M0 14a6 6 0 0 1 12 0z" fill="#17b88a"/></svg></div>
  <div class="btn" style="width:177px;height:50px">Search</div>
</form>

<h2 class="abs" style="left:111px;top:835px;font-size:34px"><span class="g">About</span> Us</h2>
<div class="abs about-text">
  <p>Browse our vacation rental selections If you are looking for a real experiences, our portal is the right solution. Our vacation homes are all located in Italy and we take care of them and their owners at every time. Our goal is give to our guest authentic taste of holiday and our country.</p>
  <p>Our team is always ready to assure the best time and take care of you! Add a local experience to your stay with us: by diving into our local "network" you can have the unique chance to discover and travel our culture through the eye of a local...!</p>
</div>
<div class="abs btn" style="left:111px;top:1128px;width:152px;height:50px">Learn More</div>
<div class="abs photo-frame"><div class="ph" role="img" aria-label="Photo of a rustic dining room with wooden beams and a laid table" style="background:linear-gradient(160deg,#6b3a1e,#c98a4a 45%,#e7d3b2 70%,#8a4a22)"></div></div>

<div class="abs band" role="img" aria-label="Faded photo of a villa garden used as section background" style="background:linear-gradient(180deg,#e3e7ea,#eef0f1 60%,#e6e9ea)"></div>
<h2 class="abs" style="left:0;width:1200px;text-align:center;top:1342px;font-size:27px"><span class="g">Looking for an</span> Exclusive Holiday</h2>

<div class="abs card" style="left:111px">
  <div class="ph" role="img" aria-label="Photo of an orange luxury villa with a swimming pool" style="background:linear-gradient(180deg,#5aa0d8,#c9753a 45%,#2fc2d6 75%,#5a8a3a)"></div>
  <h3>Luxury Villas</h3>
  <p>This selection of properties includes all the best rentals available. Most with private swimming pool with chef</p>
  <a>Learn More <svg width="13" height="13" viewBox="0 0 14 14"><circle cx="7" cy="7" r="6" fill="none" stroke="#17b88a" stroke-width="1.6"/><path d="M4 7h6M7.5 4.5 10 7l-2.5 2.5" fill="none" stroke="#17b88a" stroke-width="1.6"/></svg></a>
</div>
<div class="abs card" style="left:444px">
  <div class="ph" role="img" aria-label="Photo of a kitchen table with wine bottle and glasses" style="background:linear-gradient(180deg,#e8e2d6,#d7cbb4 55%,#7a1f22 75%,#f1eee8)"></div>
  <h3>Experiences</h3>
  <p style="padding-top:12px">Don't lve just a holiday but an experience! Let's discover our services</p>
  <a>Learn More <svg width="13" height="13" viewBox="0 0 14 14"><circle cx="7" cy="7" r="6" fill="none" stroke="#17b88a" stroke-width="1.6"/><path d="M4 7h6M7.5 4.5 10 7l-2.5 2.5" fill="none" stroke="#17b88a" stroke-width="1.6"/></svg></a>
</div>
<div class="abs card" style="left:777px">
  <div class="ph" role="img" aria-label="Photo of a rustic bedroom with wooden beams" style="background:linear-gradient(180deg,#7a4322,#e6d08a 45%,#caa060 70%,#7aa0c8)"></div>
  <h3>Browse All Vacation Rentals</h3>
  <p>From here you can browse all the villa selections, you can refine them by using the filters on the search results web page.</p>
  <a>Learn More <svg width="13" height="13" viewBox="0 0 14 14"><circle cx="7" cy="7" r="6" fill="none" stroke="#17b88a" stroke-width="1.6"/><path d="M4 7h6M7.5 4.5 10 7l-2.5 2.5" fill="none" stroke="#17b88a" stroke-width="1.6"/></svg></a>
</div>
<span class="abs dot" style="left:580px;background:#aaa"></span>
<span class="abs dot" style="left:603px;background:var(--green)"></span>

<h2 class="abs" style="left:0;width:1200px;text-align:center;top:1973px;font-size:27px"><span class="g">New Villas and</span> Vacation Rentals</h2>
<div class="abs" role="img" aria-label="Photo of a modern white villa with palm trees and a pool at dusk" style="left:153px;top:2049px;width:893px;height:504px;background:linear-gradient(180deg,#b7c4cc 0%,#d9d6cf 35%,#6a6255 55%,#2a9ed0 75%,#1778b0 100%)"></div>
<div class="abs arrow" style="left:51px;background:#f0f2f3;box-shadow:0 1px 4px rgba(0,0,0,.15)"><svg width="10" height="14"><path d="M8 1 2 7l6 6" stroke="#17b88a" stroke-width="2" fill="none"/></svg></div>
<div class="abs arrow" style="left:1113px;background:var(--green)"><svg width="10" height="14"><path d="M2 1l6 6-6 6" stroke="#fff" stroke-width="2" fill="none"/></svg></div>
<div class="abs info">
  <small>COUNTRY HOUSE / FARM HOUSE</small>
  <h3>CASA ULIVO FARMHOUSE</h3>
  <div class="meta">
    <span><svg width="16" height="11" viewBox="0 0 16 11"><path d="M0 0h2v6h14v5h-2V9H2v2H0z M3 2h4v3H3z M8 2h6a2 2 0 0 1 2 2v1H8z" fill="#17b88a"/></svg>7</span>
    <span><svg width="16" height="12" viewBox="0 0 16 12"><path d="M0 5h16v2a4 4 0 0 1-4 4H4a4 4 0 0 1-4-4z M2 0h3v5H2z" fill="#17b88a"/></svg>2</span>
  </div>
  <p>The farmhouse is immersed in the Tuscan countryside but only 3 km from the nearest town where you can find</p>
  <div class="btn" style="width:152px;height:50px;margin-top:22px">View Details</div>
</div>

<footer class="abs footer">
  <div class="abs fnav"><span>HOME</span><span>PROPERTY/UNIT</span><span>BOOKING PROCESS</span><span>BLOG STAYNEST</span><span>CONTACT US</span></div>
  <div class="abs rule" style="top:83px"></div>
  <div class="abs logo" style="left:111px;top:137px;font-size:34px"><span class="mark" style="width:30px;height:30px"></span>StayNest</div>
  <div class="abs fcol" style="left:428px;top:120px">
    <h4><span class="g">Our</span> Location</h4>
    <div class="row"><svg width="10" height="14" viewBox="0 0 10 14"><path d="M5 0a5 5 0 0 0-5 5c0 4 5 9 5 9s5-5 5-9a5 5 0 0 0-5-5zm0 7a2 2 0 1 1 0-4 2 2 0 0 1 0 4z" fill="#17b88a"/></svg><span>via dei Tigli 7 52000<br>Valdoro, Tuscany (Italy)</span></div>
  </div>
  <div class="abs fcol" style="left:696px;top:120px">
    <h4><span class="g">Contact</span> Us</h4>
    <div class="row"><svg width="14" height="14" viewBox="0 0 24 24" fill="#17b88a"><path d="M6.6 10.8a15 15 0 0 0 6.6 6.6l2.2-2.2a1 1 0 0 1 1-.25 11.4 11.4 0 0 0 3.6.57 1 1 0 0 1 1 1V20a1 1 0 0 1-1 1A17 17 0 0 1 3 4a1 1 0 0 1 1-1h3.5a1 1 0 0 1 1 1c0 1.25.2 2.45.57 3.57a1 1 0 0 1-.25 1z"/></svg><span>+39 055 0100200</span></div>
    <div class="row"><svg width="14" height="14" viewBox="0 0 14 14"><rect x="0" y="4" width="14" height="10" rx="1" fill="#17b88a"/><rect x="3" y="0" width="8" height="5" fill="#17b88a"/><rect x="3" y="7" width="8" height="1.5" fill="#000"/><rect x="3" y="10" width="8" height="1.5" fill="#000"/></svg><span>+39 055 0100300</span></div>
  </div>
  <div class="abs rule" style="top:238px"></div>
  <div class="abs" style="left:111px;top:262px;font-size:13px">Copyrights 2021 <span class="g">Stay</span>Nest. All rights reserved</div>
  <div class="abs" style="left:852px;top:262px;font-size:13px">Privacy Policy &nbsp;&nbsp;|&nbsp;&nbsp; Terms &amp; Conditions</div>
</footer>
<span class="abs social" style="left:994px"></span>
<span class="abs social" style="left:1048px"></span>

</body>
</html>
```